Webdesign für Getränkelogistik & Full-Service-Partner bei Events
Zielgruppe
Getränkelogistiker und Full-Service-Partner bei Events
Zielgruppe: Getränke-EinzelHändler; Veranstalter von Events und privaten Feiern
Aufgabenstellung
- soll „Frische“ und „Moderne“ vermitteln, ohne eine Getränkeart in den Vordergrund zu rücken
- soll von den Farben her gut zum Logo passen (siehe Anlagen)
- Slider wäre wünschenswert
- Slogan 'Wir freuen uns auf Sie!'

```html
<!DOCTYPE html>
<html lang="de">
<head>
<meta charset="utf-8">
<title>Kessler Getränke GmbH – Home</title>
<link rel="stylesheet" href="https://fonts.googleapis.com/css2?family=Open+Sans:wght@400;600;700&family=Playfair+Display:wght@700&display=swap">
<style>
  :root {
    --green: #155e52;
    --yellow: #fcc400;
    --text: #333333;
    --muted: #555555;
    --line: #cccccc;
    --white: #ffffff;
  }
  * { margin: 0; padding: 0; box-sizing: border-box; }
  html, body { width: 1146px; height: 1200px; overflow: hidden; background: var(--white); }
  body { position: relative; font-family: "Open Sans", sans-serif; color: var(--text); }

  .brand { position: absolute; top: 30px; left: 0; width: 1146px; display: flex; justify-content: center; align-items: center; gap: 10px; }
  .brand-dot { width: 26px; height: 26px; border-radius: 50%; background: var(--yellow); }
  .brand-name { font-family: "Playfair Display", serif; font-weight: 700; font-size: 26px; color: var(--green); }

  .main-nav { position: absolute; top: 90px; left: 222px; width: 702px; height: 47px; border-top: 1px solid var(--line); border-bottom: 1px solid var(--line); display: flex; justify-content: center; align-items: center; gap: 28px; font-size: 11px; }
  .main-nav a { color: var(--muted); text-decoration: none; }
  .main-nav a.active { color: var(--green); font-weight: 700; }

  .hero { position: absolute; top: 154px; left: 140px; width: 865px; height: 413px; background: linear-gradient(160deg, #c9925a 0%, #e8b25a 40%, #f8d77a 70%, #b44a22 100%); }
  .hero-slogan { position: absolute; top: 235px; left: 0; width: 364px; height: 122px; background: var(--green); padding: 16px 0 0 57px; font-family: "Playfair Display", serif; font-weight: 700; font-size: 37px; line-height: 44px; color: var(--yellow); }

  .hotline { position: absolute; top: 172px; left: 994px; width: 152px; height: 58px; background: var(--yellow); padding: 8px 0 0 11px; }
  .hotline-label { font-size: 12px; color: var(--text); }
  .hotline-number { font-size: 20px; font-weight: 700; color: var(--green); line-height: 24px; }

  .slider-dots { position: absolute; top: 580px; left: 547px; display: flex; gap: 4px; }
  .slider-dots span { width: 10px; height: 10px; border-radius: 50%; background: var(--yellow); }
  .slider-dots span.current { background: var(--green); }

  .service { position: absolute; top: 644px; width: 162px; }
  .service-label { font-size: 10.5px; font-weight: 700; color: var(--yellow); letter-spacing: .2px; }
  .service-rule { width: 30px; height: 1px; background: var(--line); margin-top: 12px; }
  .service-title { font-family: "Playfair Display", serif; font-weight: 700; font-size: 22px; color: var(--green); margin-top: 14px; white-space: nowrap; }
  .service-text { font-size: 10.5px; line-height: 16.5px; color: var(--text); margin-top: 16px; height: 82px; }
  .service-photo { height: 111px; margin-top: 7px; }
  .service-more { display: block; text-align: right; margin-top: 12px; font-size: 11px; font-weight: 700; color: var(--green); text-decoration: underline; }

  .site-footer { position: absolute; top: 1020px; left: 139px; width: 867px; height: 180px; background: var(--yellow); font-size: 11px; color: var(--text); }
  .footer-block { position: absolute; top: 40px; line-height: 21.5px; }
  .footer-block svg { position: absolute; }
  .footer-links { position: absolute; top: 49px; left: 562px; list-style: none; line-height: 21.5px; }
  .footer-links li::before { content: "• "; }
  .footer-rule { position: absolute; top: 141px; left: 83px; width: 702px; height: 1px; background: var(--white); opacity: .7; }
  .copyright { position: absolute; top: 152px; left: 0; width: 867px; text-align: center; }
</style>
</head>
<body>
  <header>
    <div class="brand"><span class="brand-dot"></span><span class="brand-name">Kessler Getränke</span></div>
    <nav class="main-nav">
      <a class="active" href="#">Home</a>
      <a href="#">Unternehmen</a>
      <a href="#">Team</a>
      <a href="#">Großhandel</a>
      <a href="#">Rund um Ihr Event</a>
      <a href="#">Karriere</a>
      <a href="#">Kontakt</a>
    </nav>
  </header>

  <section class="hero" role="img" aria-label="Zwei Flaschen werden im Gegenlicht der Sonne angestoßen">
    <div class="hero-slogan">“Wir freuen uns auf Sie!”</div>
  </section>

  <aside class="hotline">
    <div class="hotline-label">Bestell-Hotline:</div>
    <div class="hotline-number">03741 55210</div>
  </aside>

  <div class="slider-dots"><span class="current"></span><span></span><span></span><span></span></div>

  <article class="service" style="left:222px">
    <div class="service-label">SERVICE 01</div>
    <div class="service-rule"></div>
    <h2 class="service-title">Für Ihr Event</h2>
    <p class="service-text">Dies ist ein Typoblindtext. An ihm kann man sehen, ob alle Buchstaben da sind und wie sie aussehen.</p>
    <div class="service-photo" role="img" aria-label="Festzelt mit Blumenschmuck für eine Feier" style="background:linear-gradient(160deg,#2f4fb0,#8aa0d8 45%,#e8e8ee 75%,#9a9a9a)"></div>
    <a class="service-more" href="#">weiterlesen</a>
  </article>

  <article class="service" style="left:402px">
    <div class="service-label">SERVICE 02</div>
    <div class="service-rule"></div>
    <h2 class="service-title">Großhandel</h2>
    <p class="service-text">Dies ist ein Typoblindtext. An ihm kann man sehen, ob alle Buchstaben da sind und wie sie aussehen.</p>
    <div class="service-photo" role="img" aria-label="Grüne Lieferwagen-Flotte auf dem Betriebshof" style="background:linear-gradient(180deg,#dcdfe2 0%,#cfd3d5 30%,#2f5a3c 45%,#1f4a30 75%,#6a6a6a)"></div>
    <a class="service-more" href="#">weiterlesen</a>
  </article>

  <article class="service" style="left:582px">
    <div class="service-label">SERVICE 03</div>
    <div class="service-rule"></div>
    <h2 class="service-title">Unternehmen</h2>
    <p class="service-text">Dies ist ein Typoblindtext. An ihm kann man sehen, ob alle Buchstaben da sind und wie sie aussehen.</p>
    <div class="service-photo" role="img" aria-label="Geschäftsführer an einem Treppengeländer im Büro" style="background:linear-gradient(120deg,#9fa8a4,#e4e7e6 45%,#c9cccb 75%,#8e9492)"></div>
    <a class="service-more" href="#">weiterlesen</a>
  </article>

  <article class="service" style="left:762px">
    <div class="service-label">SERVICE 04</div>
    <div class="service-rule"></div>
    <h2 class="service-title">Team</h2>
    <p class="service-text">Dies ist ein Typoblindtext. An ihm kann man sehen, ob alle Buchstaben da sind und wie sie aussehen.</p>
    <div class="service-photo" role="img" aria-label="Das Team vor der Lagerhalle" style="background:linear-gradient(90deg,#c8b400,#3a3f3a 15%,#4a4f4a 50%,#3a3f3a 85%,#c8b400)"></div>
    <a class="service-more" href="#">weiterlesen</a>
  </article>

  <footer class="site-footer">
    <div class="footer-block" style="left:101px">
      <svg style="left:-18px;top:-2px" width="13" height="18" viewBox="0 0 13 18"><path d="M6.5 0C2.9 0 0 2.9 0 6.4 0 11 6.5 18 6.5 18S13 11 13 6.4C13 2.9 10.1 0 6.5 0Zm0 9A2.6 2.6 0 1 1 6.5 3.8 2.6 2.6 0 0 1 6.5 9Z" fill="#155e52"/></svg>
      Kessler Getränke GmbH<br>Lindenweg 14<br>09120 Talheim
    </div>
    <div class="footer-block" style="left:348px">
      <svg style="left:-23px;top:1px" width="16" height="16" viewBox="0 0 16 16"><path d="M3.2 0.5 5.6 3.4c.4.5.4 1.2 0 1.6L4.4 6.3c.9 2 2.6 3.8 4.7 4.9l1.3-1.2c.5-.4 1.2-.4 1.6 0l2.9 2.4c.5.4.5 1.2 0 1.7l-1.4 1.4C11.4 17.4 0 6.5 1.6 2l1.6-1.5Z" fill="#155e52"/></svg>
      Telefon: +49 3741 55210<br>Telefax: +49 3741 55211<br>
      <svg style="left:-23px;top:49px" width="16" height="12" viewBox="0 0 16 12"><rect width="16" height="12" rx="1" fill="#155e52"/><path d="M1 1.5 8 7l7-5.5" stroke="#fcc400" stroke-width="1.3" fill="none"/></svg>
      info(at)kessler-getraenke.de
    </div>
    <ul class="footer-links">
      <li>Downloads</li>
      <li>Kontakt</li>
      <li>Impressum/Datenschutz</li>
      <li>AGB</li>
    </ul>
    <div class="footer-rule"></div>
    <div class="copyright">© 2020 kessler-getraenke.de</div>
  </footer>
</body>
</html>
```